GlowRun Fundraiser

I am looking for a fresh design for the 10th annual GlowRun fundraiser. Green and blue colors need to be incorporated . I attached the current flyer. I would like this flyer for September 20, 2020. This is a fundraiser to help find a cure for NF, nuerofibromatosis.
Updates

We are looking for a fresh look for the 10th annual event

Target Market(s)

Families and individuals of surrounding areas

Colors
0255a3
add136

Requirements
Must have
• Blue and green colors. It is the 10th annual. The logos of RQ CENTER and children’s hospital logo that are shown on the previous flyer I attached
Nice to have
• Eye catching

```html
<!DOCTYPE html>
<html lang="en">
<head>
<meta charset="utf-8">
<title>GlowRun Fundraiser Flyer</title>
<link rel="stylesheet" href="https://fonts.googleapis.com/css2?family=Amatic+SC:wght@700&family=Baloo+2:wght@600;800&family=Lato:wght@400;700&family=Patrick+Hand&display=swap">
<style>
  :root {
    --blue: #233a85;
    --green: #4ab84a;
    --frame: #3b3b3d;
    --paper: #ffffff;
    --ink: #1f1f1f;
  }
  * { margin: 0; padding: 0; box-sizing: border-box; }
  html, body { width: 901px; height: 1200px; overflow: hidden; background: var(--frame); }
  .canvas { position: relative; width: 901px; height: 1200px; background: var(--frame); overflow: hidden; }
  .flyer { position: absolute; left: 88px; top: 88px; width: 726px; height: 1024px; background: var(--paper); }
  .decor { position: absolute; left: 0; top: 0; }
  .abs { position: absolute; }
  .annual { left: 132px; top: 236px; width: 104px; transform: rotate(-90deg); transform-origin: left top;
    font: 700 40px/0.85 "Amatic SC", sans-serif; color: var(--green); text-align: center; }
  .title { left: 196px; top: 106px; font: 700 225px/1 "Amatic SC", sans-serif; letter-spacing: -2px;
    white-space: nowrap; transform: scaleX(0.84); transform-origin: left top; }
  .title .b { color: var(--blue); } .title .g { color: var(--green); }
  .honoree { left: 730px; top: 156px; transform: rotate(90deg); transform-origin: left top;
    font: 700 62px/1 "Amatic SC", sans-serif; letter-spacing: 16px; color: var(--green); white-space: nowrap; }
  .tagline { left: 148px; top: 330px; width: 616px; text-align: center; font: 700 37px/1 "Amatic SC", sans-serif;
    color: var(--blue); white-space: nowrap; letter-spacing: -0.5px; }
  .tagline span { color: var(--green); }
  .when { left: 136px; top: 410px; width: 628px; text-align: center; color: var(--green); font: 800 32px/1.22 "Baloo 2", sans-serif; }
  .where { left: 136px; top: 490px; width: 628px; text-align: center; color: #fff; font: 800 19px/1.45 "Baloo 2", sans-serif; }
  .headline { left: 88px; top: 598px; width: 726px; text-align: center; color: var(--green); font: 800 40px/1 "Baloo 2", sans-serif; letter-spacing: 0.5px; }
  .activities { left: 88px; top: 652px; width: 726px; text-align: center; color: var(--ink); font: 600 20px/32px "Baloo 2", sans-serif; }
  .activities .split { position: relative; height: 32px; }
  .activities .split span { position: absolute; top: 0; }
  .activities .split .left { left: 108px; }
  .activities .split .right { left: 420px; }
  .social { left: 258px; top: 760px; width: 384px; height: 92px; border: 4px solid var(--blue); border-radius: 22px; }
  .social .dot { position: absolute; left: 40px; top: 12px; width: 62px; height: 62px; border: 3px solid var(--blue); border-radius: 50%; }
  .social .label { position: absolute; left: 116px; top: 14px; font: 48px/1 "Patrick Hand", sans-serif; color: var(--blue); letter-spacing: 1px; }
  .contact-intro { left: 88px; top: 868px; width: 726px; text-align: center; font: 700 15px/19px "Lato", sans-serif; color: var(--ink); }
  .contacts { left: 318px; top: 916px; width: 232px; text-align: right; font: 600 16px/19px "Baloo 2", sans-serif; color: var(--ink); list-style: none; }
  .partner-left { left: 160px; top: 906px; width: 130px; color: var(--blue); font: 800 34px/1 "Baloo 2", sans-serif; }
  .partner-right { left: 576px; top: 920px; width: 188px; color: var(--ink); font: 800 28px/1.05 "Baloo 2", sans-serif; text-align: center; }
  .footer-note { left: 136px; top: 1046px; width: 628px; text-align: center; color: #fff; font: 400 12px/15px "Lato", sans-serif; }
</style>
</head>
<body>
<main class="canvas">
  <section class="flyer">
    <svg class="decor" width="726" height="1024" viewBox="0 0 726 1024" aria-hidden="true">
      <path d="M0 0 H24 L27 90 L22 180 L26 270 L21 360 L25 450 L22 540 L27 630 L21 720 L26 810 L22 900 L25 960 L24 1024 H0 Z" fill="var(--green)"/>
      <path d="M726 0 H702 L699 100 L703 200 L698 300 L702 400 L699 500 L703 600 L698 700 L702 800 L699 900 L701 1024 H726 Z" fill="var(--blue)"/>
      <path d="M48 310 L80 304 L110 310 L150 303 L200 309 L260 302 L320 308 L380 301 L440 308 L500 302 L560 309 L620 300 L676 306 V484 L640 490 L590 482 L530 489 L470 483 L410 490 L350 482 L290 489 L230 483 L170 490 L110 482 L48 488 Z" fill="var(--blue)"/>
      <path d="M48 944 L90 936 L140 943 L200 935 L260 942 L320 934 L380 941 L440 935 L500 942 L560 934 L620 941 L676 936 V1024 H48 Z" fill="var(--green)"/>
    </svg>
  </section>

  <div class="abs annual">10th<br>Annual</div>
  <h1 class="abs title"><span class="b">GL</span><span class="g">O</span><span class="b">W</span><span class="g">R</span><span class="b">UN</span></h1>
  <div class="abs honoree">TESSA</div>
  <p class="abs tagline"><span>T</span>OGETHER <span>E</span>VERYONE <span>S</span>TANDS <span>S</span>TRONG <span>A</span>GAINST <span>N</span>EUROFIBROMATOSIS</p>

  <p class="abs when">Saturday September 20, 2020<br>12pm-6pm</p>
  <p class="abs where">Marlow County Fair Grounds<br>512 E, Meadowlark RD. Pinebrook, IL 62000</p>

  <h2 class="abs headline">Food, Drinks, Music &amp; Fun!!!</h2>
  <div class="abs activities">
    <p>Kids Games, Bounce House, Face Painting,</p>
    <p>Silent &amp; Live Auction, Bake Sale, Raffles</p>
    <p class="split"><span class="left">Childre's Special by</span><span class="right">12-2 walk-in appts</span></p>
  </div>

  <div class="abs social">
    <span class="dot"></span>
    <span class="label">Follow us on</span>
  </div>

  <p class="abs contact-intro">if anyone wishes to donated any items or purchase a ticket,<br>please contact one of the following people</p>
  <div class="abs partner-left">RQ CENTER</div>
  <ul class="abs contacts">
    <li>Dana Hollis: (555) 201-4417</li>
    <li>Carla Venn: (555) 318-2290</li>
    <li>Mira Olsen: (555) 462-7735</li>
    <li>Jody Pratt: (555) 590-1148</li>
  </ul>
  <div class="abs partner-right">Kidwell Hospital · Ridgeport</div>

  <p class="abs footer-note">All Proceeds donated to Kidwell Hospital Foundation<br>Riverbend University RQ Center to help find a cure!<br>Sponsored by Family &amp; Friends of T.E.S.S.A</p>
</main>
</body>
</html>
```